Application for internship at a soccer club

Task:
Template for an application for an internship at Borussia Talheim soccer club
The template should use elements that stand for the club.
eg the logo, the stadium or a stand with fans
Furthermore, the club colors should be used: https://clubhuepalette.example/borussia-talheim-color-codes/
Please use the club's font.
The design should be subtle, classy but still passionate.
The template requires space for a photo, the application text, the CV and the skills, in the proportions of the sample on the following page.
As the designer, you have creative freedom to design these elements as you see fit.
For inspiration, please take a look at the soccer club's website and browse through photos of Borussia Talheim on the Internet:
https://www.borussia-talheim.example
Sport Club

```html
<!DOCTYPE html>
<html lang="de">
<head>
<meta charset="utf-8">
<title>Bewerbung Praktikum – Borussia Talheim</title>
<link rel="stylesheet" href="https://fonts.googleapis.com/css2?family=Archivo:wght@400;500;700;800;900&display=swap">
<style>
  :root {
    --red: #e1251b;
    --black: #111111;
    --ink: #1d1d1b;
    --grey-text: #8a8a8a;
    --rule: #9d9d9d;
    --green: #3aaa35;
    --dot-grey: #b5b5b5;
    --paper: #ffffff;
  }
  * { margin: 0; padding: 0; box-sizing: border-box; }
  html, body { width: 857px; height: 1200px; overflow: hidden; background: var(--paper); }
  body { font-family: "Archivo", Arial, sans-serif; color: var(--ink); }
  .sheet { position: relative; width: 857px; height: 1200px; overflow: hidden; background: var(--paper); }

  .name { position: absolute; left: 52px; top: 52px; font-weight: 800; font-size: 54px; line-height: 48px; letter-spacing: 0.5px; color: var(--black); }
  .role { position: absolute; left: 52px; top: 174px; font-size: 19px; letter-spacing: 0.8px; color: var(--red); }

  .photo-frame { position: absolute; left: 624px; top: 18px; width: 190px; height: 190px; }
  .club-name { position: absolute; left: 500px; top: 30px; font-weight: 700; font-size: 13px; color: var(--red); letter-spacing: 0.5px; white-space: nowrap; }

  .top-rule { position: absolute; left: 52px; top: 235px; width: 762px; height: 2px; background: #6f6f6f; }
  .column-rule { position: absolute; left: 322px; top: 235px; width: 1px; height: 840px; background: #6f6f6f; }

  .side-heading { position: absolute; left: 52px; font-weight: 800; font-size: 23px; letter-spacing: 0.3px; color: var(--black); }
  .heading-rule { position: absolute; left: 52px; width: 196px; height: 2px; background: var(--rule); }
  .heading-rule::before { content: ""; position: absolute; left: 0; top: -1px; width: 50px; height: 4px; background: var(--red); }

  .contact-item { position: absolute; left: 52px; display: flex; align-items: center; gap: 19px; font-size: 13px; letter-spacing: 0.6px; }
  .contact-icon { width: 29px; height: 29px; background: var(--black); display: flex; align-items: center; justify-content: center; }

  .interest { position: absolute; left: 50px; width: 200px; display: flex; align-items: center; justify-content: space-between; font-size: 13px; line-height: 14px; }
  .rating { display: flex; gap: 2px; }

  .skill { position: absolute; left: 52px; width: 196px; font-size: 13px; }
  .skill-bar { position: absolute; left: 74px; top: 8px; width: 122px; height: 2px; background: var(--rule); }
  .skill-fill { position: absolute; left: 0; top: -1px; height: 4px; background: var(--red); }
  .skill-fill::after { content: ""; position: absolute; right: -1px; top: -3px; width: 2px; height: 10px; background: var(--red); }

  .podcast { position: absolute; left: 52px; font-size: 13px; }
  .podcast::before { content: "›"; color: var(--red); font-weight: 700; font-size: 18px; margin-right: 5px; position: relative; top: 1px; }

  .greeting { position: absolute; left: 363px; top: 264px; font-weight: 700; font-size: 21px; color: #333; }
  .intro { position: absolute; left: 363px; top: 298px; width: 451px; font-size: 11.3px; line-height: 16.8px; color: #333; text-align: justify; }

  .main-heading { position: absolute; left: 363px; top: 447px; font-weight: 800; font-size: 26px; letter-spacing: 0.5px; color: var(--black); }
  .main-rule { position: absolute; left: 363px; top: 480px; width: 451px; height: 2px; background: var(--rule); }
  .main-rule::before { content: ""; position: absolute; left: 0; top: -1px; width: 50px; height: 4px; background: var(--red); }

  .entry-head { position: absolute; left: 363px; width: 451px; display: flex; justify-content: space-between; font-size: 13px; color: #222; }
  .entry-body { position: absolute; left: 363px; width: 451px; font-size: 10.6px; line-height: 16.8px; color: var(--grey-text); text-align: justify; }

  .footer-art { position: absolute; left: 0; top: 0; width: 857px; height: 1200px; pointer-events: none; }
</style>
</head>
<body>
<main class="sheet">

  <h1 class="name">Name<br>SURNAME</h1>
  <p class="role">Application for an internship</p>

  <span class="club-name">Borussia Talheim</span>
  <svg class="photo-frame" viewBox="0 0 190 190" role="img" aria-label="Platz für das Bewerbungsfoto">
    <circle cx="95" cy="95" r="90" fill="none" stroke="var(--red)" stroke-width="4.5"/>
    <circle cx="95" cy="95" r="80" fill="none" stroke="var(--red)" stroke-width="1.8"/>
    <rect x="76" y="81" width="38" height="28" rx="2" fill="var(--red)"/>
    <rect x="84" y="76" width="13" height="6" fill="var(--red)"/>
    <circle cx="95" cy="95" r="8" fill="#fff"/>
    <circle cx="95" cy="95" r="5" fill="var(--red)"/>
  </svg>

  <div class="top-rule"></div>
  <div class="column-rule"></div>

  <!-- Contact -->
  <h2 class="side-heading" style="top:265px">CONTACT</h2>
  <div class="heading-rule" style="top:303px"></div>

  <div class="contact-item" style="top:322px">
    <span class="contact-icon"><svg width="16" height="16" viewBox="0 0 24 24"><path fill="#fff" d="M6.6 10.8a15.1 15.1 0 0 0 6.6 6.6l2.2-2.2c.3-.3.7-.4 1-.2 1.1.4 2.3.6 3.6.6.6 0 1 .4 1 1V20c0 .6-.4 1-1 1A17 17 0 0 1 3 4c0-.6.4-1 1-1h3.5c.6 0 1 .4 1 1 0 1.3.2 2.5.6 3.6.1.3 0 .7-.2 1z"/></svg></span>
    <span>+000 12345 6789</span>
  </div>
  <div class="contact-item" style="top:377px">
    <span class="contact-icon"><svg width="16" height="12" viewBox="0 0 16 12"><rect x="0.5" y="0.5" width="15" height="11" fill="#fff"/><path d="M0.5 0.5 8 7l7.5-6.5" fill="none" stroke="#111" stroke-width="1.2"/></svg></span>
    <span>loremipsum@postfach.example</span>
  </div>
  <div class="contact-item" style="top:431px">
    <span class="contact-icon"><svg width="17" height="17" viewBox="0 0 20 20" fill="none" stroke="#fff" stroke-width="1.5"><circle cx="10" cy="10" r="8.5"/><ellipse cx="10" cy="10" rx="3.8" ry="8.5"/><path d="M1.5 10h17M3 5.5h14M3 14.5h14"/></svg></span>
    <span>www.loremipsum.example</span>
  </div>

  <!-- Interests -->
  <h2 class="side-heading" style="top:506px">INTERESSEN</h2>
  <div class="heading-rule" style="top:544px"></div>

  <div class="interest" style="top:568px"><span>Borussia<br>Talheim</span><span class="rating">
    <svg width="80" height="14" viewBox="0 0 80 14"><g fill="var(--green)"><circle cx="7" cy="7" r="6.5"/><circle cx="23" cy="7" r="6.5"/><circle cx="39" cy="7" r="6.5"/><circle cx="55" cy="7" r="6.5"/><circle cx="71" cy="7" r="6.5"/></g><g fill="none" stroke="#fff" stroke-width="1.6"><path d="M4 7l2 2 4-4M20 7l2 2 4-4M36 7l2 2 4-4M52 7l2 2 4-4M68 7l2 2 4-4"/></g></svg></span></div>
  <div class="interest" style="top:613px"><span>Landesliga</span><span class="rating">
    <svg width="80" height="14" viewBox="0 0 80 14"><g fill="var(--green)"><circle cx="7" cy="7" r="6.5"/><circle cx="23" cy="7" r="6.5"/><circle cx="39" cy="7" r="6.5"/><circle cx="55" cy="7" r="6.5"/><circle cx="71" cy="7" r="6.5"/></g><g fill="none" stroke="#fff" stroke-width="1.6"><path d="M4 7l2 2 4-4M20 7l2 2 4-4M36 7l2 2 4-4M52 7l2 2 4-4M68 7l2 2 4-4"/></g></svg></span></div>
  <div class="interest" style="top:653px"><span>Europäische<br>Ligen</span><span class="rating">
    <svg width="80" height="14" viewBox="0 0 80 14"><g fill="var(--green)"><circle cx="7" cy="7" r="6.5"/><circle cx="23" cy="7" r="6.5"/><circle cx="39" cy="7" r="6.5"/><circle cx="55" cy="7" r="6.5"/></g><circle cx="71" cy="7" r="6.5" fill="var(--dot-grey)"/><g fill="none" stroke="#fff" stroke-width="1.6"><path d="M4 7l2 2 4-4M20 7l2 2 4-4M36 7l2 2 4-4M52 7l2 2 4-4M67.5 7h7"/></g></svg></span></div>
  <div class="interest" style="top:695px"><span>Radsport</span><span class="rating">
    <svg width="80" height="14" viewBox="0 0 80 14"><g fill="var(--green)"><circle cx="7" cy="7" r="6.5"/><circle cx="23" cy="7" r="6.5"/><circle cx="39" cy="7" r="6.5"/><circle cx="55" cy="7" r="6.5"/></g><circle cx="71" cy="7" r="6.5" fill="var(--red)"/><g fill="none" stroke="#fff" stroke-width="1.6"><path d="M4 7l2 2 4-4M20 7l2 2 4-4M36 7l2 2 4-4M52 7l2 2 4-4M68.5 4.5l5 5M73.5 4.5l-5 5"/></g></svg></span></div>
  <div class="interest" style="top:731px"><span>Triathlon</span><span class="rating">
    <svg width="80" height="14" viewBox="0 0 80 14"><g fill="var(--green)"><circle cx="7" cy="7" r="6.5"/><circle cx="23" cy="7" r="6.5"/><circle cx="39" cy="7" r="6.5"/><circle cx="55" cy="7" r="6.5"/></g><circle cx="71" cy="7" r="6.5" fill="var(--red)"/><g fill="none" stroke="#fff" stroke-width="1.6"><path d="M4 7l2 2 4-4M20 7l2 2 4-4M36 7l2 2 4-4M52 7l2 2 4-4M68.5 4.5l5 5M73.5 4.5l-5 5"/></g></svg></span></div>

  <!-- Skills -->
  <h2 class="side-heading" style="top:777px">KENNTNISSE</h2>
  <div class="heading-rule" style="top:810px"></div>
  <div class="skill" style="top:830px">Englisch<div class="skill-bar"><div class="skill-fill" style="width:116px"></div></div></div>
  <div class="skill" style="top:860px">Bürotools<div class="skill-bar"><div class="skill-fill" style="width:98px"></div></div></div>

  <!-- Podcasts -->
  <h2 class="side-heading" style="top:911px;font-size:19px">PODCAST ABO´S:</h2>
  <div class="heading-rule" style="top:942px"></div>
  <p class="podcast" style="top:958px">Talheimer Kurve</p>
  <p class="podcast" style="top:989px">Borussia Talheim Podcast</p>
  <p class="podcast" style="top:1020px">Einfach mal Kicken</p>

  <!-- Main column -->
  <h2 class="greeting">Hello, I’m Name</h2>
  <p class="intro">My Name lorem empus id fringilla molestie ornare diam in olestie ipsum etiam rosn ollicitudin est, porttitor amet hitmassa Done cporttitor dolor shit dolor kiren lorem nisl molestie pretium etfring. is the shitp lorem ipcum retiumci amet is tudinest moles tium lorem olestie pretium apaza all the rosen. fringilla lorem ipsum.<br>orem nisl molestie pretium etfring. is the shitp lorem ipcum retiumci amet is tudinest moles tium lorem olestie pretium apaza all the rosen. fringilla lorem ipsum.</p>

  <h2 class="main-heading">EXPERIENCE</h2>
  <div class="main-rule"></div>

  <div class="entry-head" style="top:515px"><span>High school &nbsp;|&nbsp; Location</span><span>09.2016 - 06.2024</span></div>
  <p class="entry-body" style="top:540px">Lorem ipsum dolor sit amet, consectetuer adipiscing elit, sed diam nonummy nibh euismod tincidunt ut laoreet dolore magna aliquam erat volutpat. Ut wisi enim ad minim veniam, quis nostrud exerci tation ullamcorper suscipit lobortis nisl ut aliquip ex ea commodo consequat. Duis autem vel eum iriure dolor in hendrerit in vulputate velit esse molestie consequat, vel illum dolore eu feugiat nulla facilisis at vero eros et accumsan et iusto odio dignissim qui blandit praesent luptatum zzril delenit augue duis dolore te feugait nulla facilisi. dolor sit amet, consectetuer adipiscing elit, sed diam nonummy nibh dolor sit amet, consectetuer adipiscing elit, sed diam nonummy nibh</p>

  <div class="entry-head" style="top:718px"><span>Elementary school &nbsp;|&nbsp; Location</span><span>08.2012 - 07.2016</span></div>
  <p class="entry-body" style="top:743px">Lorem ipsum dolor sit amet, consectetuer adipiscing elit, sed diam nonummy nibh euismod tincidunt ut laoreet dolore magna aliquam erat volutpat. Ut wisi enim ad minim veniam, quis nostrud exerci tation ullamcorper suscipit lobortis nisl ut aliquip ex ea commodo consequat. Duis autem vel eum iriure dolor in hendrerit in vulputate velit esse molestie consequat, vel illum dolore eu feugiat nulla facilisis at vero eros et accumsan et iusto odio dignissim qui blandit praesent luptatum zzril delenit augue duis dolore te feugait nulla facilisi. dolor sit amet, consectetuer adipiscing elit, sed diam nonummy nibh dolor sit amet, consectetuer adipiscing elit, sed diam nonummy nibh</p>

  <!-- Footer band -->
  <svg class="footer-art" viewBox="0 0 857 1200">
    <defs>
      <linearGradient id="stand-tone" x1="0" y1="0" x2="1" y2="1">
        <stop offset="0" stop-color="#1c1c1c"/>
        <stop offset="0.5" stop-color="#2b2b2b"/>
        <stop offset="1" stop-color="#141414"/>
      </linearGradient>
    </defs>
    <polygon points="0,1098 857,920 857,1200 0,1200" fill="var(--red)"/>
    <polygon points="0,1132 857,952 857,1200 0,1200" fill="url(#stand-tone)" role="img" aria-label="Dunkle Fläche für ein Tribünen- und Fanmotiv des Vereins"/>
  </svg>

</main>
</body>
</html>
```